Lumora Flow Collective Business Cards

I need business cards for staff in a new startup. Our company name is MorvaLeap - we train Tai Chi teachers. But our biggest project is called Lumora Flow Collective - a federal project to put together free Tai Chi classes for Vets all across America. It's a young company, with a spirit of excitement, passion, a desire to do good for others (our Vets) and a modern style and sensibility. In other words, not old-fashioned Asian martial arts theme, but something new.

Industry/Entity Type

Health And Wellness

Contact Information for Business Card

The topic is ancient healing, but the company is the Quibbletons - so I'd like a card design that captures that.

Font styles to use
Sans Serif

Colors

Designer to choose colors to be used in the design.

Requirements
Nice to have
• I've got two logos - one for the company and one for the project. I want to see if we can incorporate them both without it becoming too busy.
Should not have
• Overly old-fashioned yin-yang themes.

```html
<!DOCTYPE html>
<html lang="en">
<head>
<meta charset="utf-8">
<title>Lumora Flow Collective Business Cards</title>
<link href="https://fonts.googleapis.com/css2?family=Montserrat:wght@300&family=Open+Sans:wght@400;600&family=Tinos:wght@700&display=swap" rel="stylesheet">
<style>
  :root {
    --backdrop: #8a8a8a;
    --card: #1c1b1c;
    --card-soft: #242324;
    --gold: #c9a27a;
    --red: #d7192a;
    --white: #f2f2f2;
  }
  * { margin: 0; padding: 0; box-sizing: border-box; }
  html, body { width: 1200px; height: 1021px; overflow: hidden; }
  body {
    background: var(--backdrop);
    position: relative;
    font-family: "Open Sans", sans-serif;
  }
  .card {
    position: absolute;
    left: 160px;
    width: 880px;
    height: 440px;
    background: var(--card);
    box-shadow: 0 14px 30px rgba(0,0,0,.35);
    overflow: hidden;
  }
  .card--front { top: 50px; }
  .card--back { top: 531px; }

  .figure-art {
    position: absolute;
    background: var(--card-soft);
    border-radius: 40px 40px 8px 8px;
  }
  .figure-art--left { left: 70px; top: 40px; width: 220px; height: 300px; }
  .figure-art--right { right: 70px; top: 130px; width: 240px; height: 300px; }

  .project-mark {
    position: absolute;
    left: 50%; top: 50%;
    transform: translate(-50%, -50%);
    display: flex;
    align-items: center;
    gap: 26px;
  }
  .project-mark__dot {
    width: 110px; height: 110px;
    border: 2px solid var(--gold);
    border-radius: 50%;
  }
  .project-mark__name {
    font-family: "Montserrat", sans-serif;
    font-weight: 300;
    font-size: 34px;
    letter-spacing: 3px;
    text-transform: uppercase;
    color: var(--gold);
    line-height: 1.2;
  }

  .company-mark {
    position: absolute;
    left: 70px; top: 120px;
    display: flex;
    align-items: center;
    gap: 20px;
  }
  .company-mark__dot {
    width: 120px; height: 120px;
    border-radius: 50%;
    background: var(--red);
  }
  .company-mark__name {
    font-size: 36px;
    font-weight: 600;
    color: var(--red);
  }

  .contact {
    position: absolute;
    left: 470px; top: 90px;
    color: var(--white);
  }
  .contact__name {
    font-family: "Tinos", serif;
    font-weight: 700;
    font-size: 28px;
    color: var(--red);
    line-height: 1.1;
  }
  .contact__role { font-size: 19px; margin-bottom: 50px; }
  .contact__address { font-size: 19px; line-height: 1.3; margin-bottom: 8px; }
  .contact__line {
    display: flex; align-items: center; gap: 12px;
    font-size: 19px; line-height: 1.45;
  }
  .contact__line svg { width: 18px; height: 18px; flex: none; }
</style>
</head>
<body>

<section class="card card--front">
  <div class="figure-art figure-art--left" role="img" aria-label="Faint silhouette of a tai chi practitioner in a stance"></div>
  <div class="figure-art figure-art--right" role="img" aria-label="Faint silhouette of a tai chi practitioner in a wide stance"></div>
  <div class="project-mark">
    <span class="project-mark__dot"></span>
    <span class="project-mark__name">Lumora Flow<br>Collective</span>
  </div>
</section>

<section class="card card--back">
  <div class="company-mark">
    <span class="company-mark__dot"></span>
    <span class="company-mark__name">MorvaLeap</span>
  </div>

  <div class="contact">
    <p class="contact__name">Corin Valemont-Ashby</p>
    <p class="contact__role">Founder</p>
    <p class="contact__address">4127 Ferrow Ave. Ste. 212<br>Brightmoor Bay, CA 90417</p>
    <p class="contact__line">
      <svg viewBox="0 0 24 24" aria-hidden="true"><path fill="#d7192a" d="M6.6 10.8a15 15 0 0 0 6.6 6.6l2.2-2.2a1 1 0 0 1 1-.25 11.4 11.4 0 0 0 3.6.57 1 1 0 0 1 1 1V20a1 1 0 0 1-1 1A17 17 0 0 1 3 4a1 1 0 0 1 1-1h3.5a1 1 0 0 1 1 1c0 1.25.2 2.45.57 3.57a1 1 0 0 1-.25 1z"/></svg>
      555-018-2746
    </p>
    <p class="contact__line">
      <svg viewBox="0 0 24 24" aria-hidden="true"><rect x="2.5" y="5" width="19" height="14" fill="none" stroke="#d7192a" stroke-width="2"/><path d="M3 6l9 7 9-7" fill="none" stroke="#d7192a" stroke-width="2"/></svg>
      info@morvaleap.net
    </p>
    <p class="contact__line">
      <svg viewBox="0 0 24 24" aria-hidden="true"><g fill="none" stroke="#d7192a" stroke-width="1.8"><circle cx="12" cy="12" r="9.5"/><ellipse cx="12" cy="12" rx="4.5" ry="9.5"/><path d="M2.5 12h19M4 7h16M4 17h16"/></g></svg>
      www.morvaleap.net
    </p>
  </div>
</section>

</body>
</html>
```